Vesna Architecture

We are a architectural design and build company working between scales 1/1000 to 1/1 we want people to understand our difference from our design experience and quality.we build hotels restourants and office spaces.Our company name is Vesna architecture to mind sustainability.

We want to write our adress phone and work spesifications on the card and we want our logo as backround.

Ps:you could find the logo adress and phone box numbers from the web:www.vesnayapi.example

Target Market(s)

Who looks for experts.

Industry/Entity Type

Architecture

Requirements
Must have
• Design is over everything.
Should not have
• we don want it to be colorfull

```html
<!DOCTYPE html>
<html lang="tr">
<head>
<meta charset="utf-8">
<title>Vesna Architecture – Business Card</title>
<link rel="stylesheet" href="https://fonts.googleapis.com/css2?family=Questrial&family=Arimo&display=swap">
<style>
  :root {
    --backdrop: #1d1d1d;
    --card-light: #ffffff;
    --card-edge: #cfcfcf;
    --ink: #111111;
    --ink-soft: #6a6a6a;
    --ghost: rgba(0, 0, 0, 0.06);
    --contact-blue: #8fd0ec;
  }
  * { margin: 0; padding: 0; box-sizing: border-box; }
  html, body { width: 1200px; height: 750px; overflow: hidden; background: var(--backdrop); }
  .canvas { position: relative; width: 1200px; height: 750px; }

  .card {
    position: absolute;
    overflow: hidden;
    background: radial-gradient(ellipse at 60% 20%, var(--card-light) 0%, #ececec 45%, var(--card-edge) 100%);
  }
  .card--front { left: 52px; top: 71px; width: 485px; height: 277px; }
  .card--back  { left: 622px; top: 228px; width: 512px; height: 293px; }

  .wordmark {
    position: absolute;
    font-family: "Questrial", sans-serif;
    color: var(--ink);
    line-height: 1;
    white-space: nowrap;
  }
  .wordmark__name { display: block; text-transform: lowercase; letter-spacing: -2px; }
  .wordmark__sub  { display: block; letter-spacing: 3px; }

  .card--front .wordmark { left: 106px; top: 28px; }
  .card--front .wordmark__name { font-size: 118px; }
  .card--front .wordmark__sub  { font-size: 26px; margin-top: 30px; margin-left: 2px; }

  .card--back .wordmark--small { left: 7px; top: 6px; }
  .card--back .wordmark--small .wordmark__name { font-size: 34px; letter-spacing: -1px; }
  .card--back .wordmark--small .wordmark__sub  { font-size: 8px; letter-spacing: 1px; margin-top: 3px; margin-left: 1px; }

  .card--back .wordmark--ghost { left: 110px; top: 40px; color: var(--ghost); }
  .card--back .wordmark--ghost .wordmark__name { font-size: 124px; }
  .card--back .wordmark--ghost .wordmark__sub  { font-size: 30px; margin-top: 32px; margin-left: 2px; }

  .website {
    position: absolute;
    font-family: "Questrial", sans-serif;
    font-size: 8px;
    letter-spacing: 4px;
    color: var(--ink-soft);
    white-space: nowrap;
  }
  .card--front .website { left: 258px; top: 232px; }
  .card--back .website  { left: 182px; top: 254px; }

  .contact {
    position: absolute;
    left: 202px; top: 73px;
    width: 310px; height: 152px;
    background: var(--contact-blue);
    box-shadow: -2px 3px 8px rgba(0, 0, 0, 0.35);
    padding: 30px 0 0 36px;
    font-family: "Arimo", sans-serif;
    font-size: 12.5px;
    line-height: 15px;
    color: var(--ink);
  }
  .contact__name { margin-bottom: 15px; }
</style>
</head>
<body>
<main class="canvas">
  <section class="card card--front" aria-label="Card front">
    <div class="wordmark">
      <span class="wordmark__name">vesna</span>
      <span class="wordmark__sub">MİMARLIK</span>
    </div>
    <p class="website">www.vesnayapi.example</p>
  </section>

  <section class="card card--back" aria-label="Card back">
    <div class="wordmark wordmark--ghost" aria-hidden="true">
      <span class="wordmark__name">vesna</span>
      <span class="wordmark__sub">MİMARLIK</span>
    </div>
    <div class="wordmark wordmark--small">
      <span class="wordmark__name">vesna</span>
      <span class="wordmark__sub">MİMARLIK</span>
    </div>
    <div class="contact">
      <p class="contact__name">Deniz Arman KAYA - Mimar</p>
      <p>(Mimar-Architect)</p>
      <p>Lalezar Mah. Deniz Cad. Ilgın Sok.</p>
      <p>No : 8 Yeldeğirmeni / ISTANBUL</p>
      <p>Telephone. 0216 555 01 40 , 0216 555 01 72</p>
    </div>
    <p class="website">www.vesnayapi.example</p>
  </section>
</main>
</body>
</html>
```